Business cards

I would like a black background with the design I previously chose. I need 2 sets of cards. Mine will have Marisol Brandt, Broker/Owner, 307-555-0148 and marisol.harborpeak@mailvista.com
The second set will read, Dana Rutledge, Realtor 307-555-0172, dana.harborpeak@mailvista.com

Industry/Entity Type

Business

```html
<!DOCTYPE html>
<html lang="en">
<head>
<meta charset="utf-8">
<title>Business Card – Marisol Brandt</title>
<link href="https://fonts.googleapis.com/css2?family=Delius&display=swap" rel="stylesheet">
<style>
  :root {
    --page-bg: #e4e2df;
    --card-bg: #0b0c0c;
    --ink: #ece8e2;
    --rule: #8d8a86;
    --icon-fg: #0b0c0c;
  }
  * { box-sizing: border-box; margin: 0; padding: 0; }
  html, body {
    width: 1200px;
    height: 1200px;
    overflow: hidden;
    background: var(--page-bg);
  }
  .canvas {
    width: 1200px;
    height: 1200px;
    display: flex;
    align-items: center;
    justify-content: center;
  }
  .card {
    position: relative;
    width: 1000px;
    height: 571px;
    background: var(--card-bg);
    font-family: "Delius", sans-serif;
    color: var(--ink);
    box-shadow: 0 12px 30px rgba(0,0,0,0.25);
  }
  .identity {
    position: absolute;
    right: 578px;
    top: 272px;
    text-align: right;
  }
  .identity__name {
    font-size: 42px;
    letter-spacing: 0.5px;
    line-height: 1.1;
    text-transform: uppercase;
    white-space: nowrap;
  }
  .identity__title {
    font-size: 30px;
    line-height: 1.3;
    margin-top: 2px;
    white-space: nowrap;
  }
  .divider {
    position: absolute;
    left: 440px;
    top: 260px;
    width: 2px;
    height: 110px;
    background: var(--rule);
  }
  .contact {
    position: absolute;
    left: 462px;
    top: 262px;
    list-style: none;
  }
  .contact__item {
    display: flex;
    align-items: center;
    gap: 10px;
    font-size: 29px;
    line-height: 1.45;
    white-space: nowrap;
  }
  .contact__icon {
    width: 26px;
    height: 26px;
    flex: none;
  }
</style>
</head>
<body>
  <main class="canvas">
    <section class="card" aria-label="Business card">
      <div class="identity">
        <p class="identity__name">Marisol Brandt</p>
        <p class="identity__title">Broker/Owner</p>
      </div>
      <div class="divider"></div>
      <ul class="contact">
        <li class="contact__item">
          <svg class="contact__icon" viewBox="0 0 26 26" aria-hidden="true">
            <rect width="26" height="26" rx="4" fill="var(--ink)"/>
            <path d="M5 10 Q13 4 21 10 L19 12 L16 10 L10 10 L7 12 Z" fill="var(--icon-fg)"/>
            <path d="M8 13 L18 13 L20 20 L6 20 Z" fill="var(--icon-fg)"/>
            <circle cx="13" cy="16.5" r="2" fill="var(--ink)"/>
          </svg>
          <span class="contact__text">307-555-0148</span>
        </li>
        <li class="contact__item">
          <svg class="contact__icon" viewBox="0 0 26 26" aria-hidden="true">
            <rect width="26" height="26" rx="4" fill="var(--ink)"/>
            <rect x="5" y="7" width="16" height="12" fill="var(--icon-fg)"/>
            <path d="M5 7 L13 14 L21 7" fill="none" stroke="var(--ink)" stroke-width="1.5"/>
          </svg>
          <span class="contact__text">marisol.harborpeak@mailvista.com</span>
        </li>
      </ul>
    </section>
  </main>
</body>
</html>
```